Apple and Cherry Distrubuter looking for a new Branded design for cherry and apple boxes.

Rowlett Fruit Packers is a company that grows cherries and apples in their family owned and operated orchards. Pack at their own facilities using state of the art equipment. Sell the fruit across the world and distribute within North America. Our company is based out of Kelowna British Columbia, Canada in the Okanagan Valley.Furthermore we are looking for our own branded company box one for cherries with designs around our Logo implemented with the cherry fruit and concepts of blossoms and grown in Canada. The same will be done for the apple branded box.

Logo Text

Use our company logo. Implement something similar to From our family to yours and maybe add Legacy Quality

Colors

Designer to choose colors to be used in the design.

Requirements
Must have
• Our Logo has to be implemented.
• A slogan similar or more creative to From our Family to Yours
• Legacy Quality
• Emphasis on Canadian.
• Unique designs that show an elegant premium brand. Realistic pictures
Nice to have
• Think Professional. Elegant and supreme to other packers.
• Maybe even a white back ground with blended designs of blossoms in white and pink... with the blossoms scattered across our company logo as if someone had blow the box off.

```html
<!DOCTYPE html>
<html lang="en">
<head>
<meta charset="utf-8">
<title>Rowlett Fruit Packers – Cherry and Apple Box Panels</title>
<link href="https://fonts.googleapis.com/css2?family=Baloo+2:wght@600&family=Open+Sans:wght@400&display=swap" rel="stylesheet">
<style>
  :root {
    --stage: #e6e6e6;
    --stage-light: #f4f4f4;
    --brand-green: #3cbf2e;
    --muted-grey: #7a7a7a;
    --cherry-pink: #fbb6d6;
    --apple-green: #bfe860;
    --white: #ffffff;
    --cherry-red: #d5121d;
    --leaf-green: #4d9a2a;
    --apple-red: #d9231a;
  }
  * { margin: 0; padding: 0; box-sizing: border-box; }
  html, body { width: 1200px; height: 1200px; overflow: hidden; }
  body {
    background: radial-gradient(ellipse at 50% 50%, var(--stage-light), var(--stage));
    position: relative;
  }
  .panel {
    position: absolute;
    overflow: hidden;
    background: var(--white);
  }
  .cherry.top-row   { background: linear-gradient(180deg, var(--cherry-pink) 0%, var(--white) 35%, var(--white) 100%); }
  .cherry.bottom-row{ background: linear-gradient(180deg, var(--white) 0%, var(--white) 62%, var(--cherry-pink) 82%); }
  .apple.top-row    { background: linear-gradient(180deg, var(--apple-green) 0%, var(--white) 30%, var(--white) 100%); }
  .apple.bottom-row { background: linear-gradient(180deg, var(--white) 0%, var(--white) 62%, var(--apple-green) 80%); }

  .brand {
    position: absolute;
    left: 0; right: 0;
    text-align: center;
  }
  .wordmark {
    font-family: "Baloo 2", sans-serif;
    font-weight: 600;
    color: var(--brand-green);
    font-size: 14px;
    line-height: 1.05;
  }
  .wordmark-dot {
    display: block;
    width: 34px; height: 34px;
    margin: 0 auto 6px;
    border-radius: 50%;
    background: var(--brand-green);
  }
  .slogan {
    font-family: "Baloo 2", sans-serif;
    font-weight: 600;
    color: var(--brand-green);
    font-size: 16px;
    margin-top: 18px;
  }
  .legacy {
    font-family: "Open Sans", sans-serif;
    color: var(--muted-grey);
    font-size: 8px;
    letter-spacing: 0.3px;
    margin-top: 2px;
  }
  .photo {
    position: absolute;
    border-radius: 50%;
  }
  .cherry .photo { background: radial-gradient(circle at 40% 40%, #f0444a, var(--cherry-red) 60%, rgba(213,18,29,0) 72%); }
  .cherry .photo.blossom { background: radial-gradient(circle, #fde3ee, #f7b4cf 55%, rgba(247,180,207,0) 72%); }
  .apple .photo { background: radial-gradient(circle at 40% 40%, #f05a3a, var(--apple-red) 60%, rgba(217,35,26,0) 72%); }
  .apple .photo.green-apple { background: radial-gradient(circle, #6fd83a, #3fb51c 60%, rgba(63,181,28,0) 72%); }
  .apple .photo.blossom { background: radial-gradient(circle, #ffffff, #f4d0de 55%, rgba(244,208,222,0) 72%); }
  .photo.soft { filter: blur(4px); }
  .photo.leaf { border-radius: 60% 0; background: var(--leaf-green); opacity: .85; }
</style>
</head>
<body>

<!-- Cherry box -->
<section class="box cherry-box">
  <div class="panel cherry top-row" style="left:30px;top:66px;width:232px;height:232px">
    <div class="photo soft" style="left:-20px;top:40px;width:70px;height:90px" role="img" aria-label="Cluster of ripe red cherries"></div>
    <div class="photo" style="left:18px;top:180px;width:50px;height:40px" role="img" aria-label="Pair of cherries on stems"></div>
    <div class="photo" style="left:178px;top:165px;width:30px;height:30px" role="img" aria-label="Single cherry on stem"></div>
    <div class="photo blossom" style="left:186px;top:70px;width:36px;height:36px" role="img" aria-label="Pink cherry blossom"></div>
    <div class="photo leaf soft" style="left:180px;top:195px;width:60px;height:30px" role="img" aria-label="Green leaf"></div>
    <div class="brand" style="top:80px"><span class="wordmark-dot"></span><div class="wordmark">Rowlett<br>Fruit Packers</div></div>
  </div>
  <div class="panel cherry top-row" style="left:266px;top:66px;width:330px;height:232px">
    <div class="photo" style="left:22px;top:50px;width:70px;height:60px" role="img" aria-label="Cherries on a branch with leaves"></div>
    <div class="photo soft" style="left:10px;top:185px;width:55px;height:55px" role="img" aria-label="Blurred cherry"></div>
    <div class="photo" style="left:18px;top:135px;width:30px;height:30px" role="img" aria-label="Single cherry"></div>
    <div class="photo blossom" style="left:225px;top:0px;width:40px;height:36px" role="img" aria-label="Pink blossom"></div>
    <div class="photo soft" style="left:270px;top:80px;width:60px;height:80px" role="img" aria-label="Blurred cherries"></div>
    <div class="photo" style="left:250px;top:170px;width:60px;height:45px" role="img" aria-label="Pair of cherries"></div>
    <div class="brand" style="top:50px"><span class="wordmark-dot"></span><div class="wordmark">Rowlett<br>Fruit Packers</div><div class="slogan">From our family to yours</div><div class="legacy">LEGACY QUALITY</div></div>
  </div>
  <div class="panel cherry top-row" style="left:602px;top:66px;width:232px;height:232px">
    <div class="photo soft" style="left:-20px;top:40px;width:70px;height:90px" role="img" aria-label="Cluster of ripe red cherries"></div>
    <div class="photo" style="left:18px;top:180px;width:50px;height:40px" role="img" aria-label="Pair of cherries on stems"></div>
    <div class="photo" style="left:178px;top:165px;width:30px;height:30px" role="img" aria-label="Single cherry on stem"></div>
    <div class="photo blossom" style="left:186px;top:70px;width:36px;height:36px" role="img" aria-label="Pink cherry blossom"></div>
    <div class="photo leaf soft" style="left:180px;top:195px;width:60px;height:30px" role="img" aria-label="Green leaf"></div>
    <div class="brand" style="top:80px"><span class="wordmark-dot"></span><div class="wordmark">Rowlett<br>Fruit Packers</div></div>
  </div>
  <div class="panel cherry top-row" style="left:838px;top:66px;width:330px;height:232px">
    <div class="photo" style="left:22px;top:50px;width:70px;height:60px" role="img" aria-label="Cherries on a branch with leaves"></div>
    <div class="photo soft" style="left:10px;top:185px;width:55px;height:55px" role="img" aria-label="Blurred cherry"></div>
    <div class="photo" style="left:18px;top:135px;width:30px;height:30px" role="img" aria-label="Single cherry"></div>
    <div class="photo blossom" style="left:225px;top:0px;width:40px;height:36px" role="img" aria-label="Pink blossom"></div>
    <div class="photo soft" style="left:270px;top:80px;width:60px;height:80px" role="img" aria-label="Blurred cherries"></div>
    <div class="photo" style="left:250px;top:170px;width:60px;height:45px" role="img" aria-label="Pair of cherries"></div>
    <div class="brand" style="top:50px"><span class="wordmark-dot"></span><div class="wordmark">Rowlett<br>Fruit Packers</div><div class="slogan">From our family to yours</div><div class="legacy">LEGACY QUALITY</div></div>
  </div>

  <div class="panel cherry bottom-row" style="left:30px;top:304px;width:232px;height:233px">
    <div class="photo blossom" style="left:10px;top:80px;width:36px;height:40px" role="img" aria-label="Pink blossoms"></div>
    <div class="photo" style="left:26px;top:140px;width:50px;height:45px" role="img" aria-label="Cherries on stems"></div>
    <div class="photo soft" style="left:176px;top:115px;width:45px;height:45px" role="img" aria-label="Blurred cherry"></div>
    <div class="photo blossom" style="left:170px;top:170px;width:50px;height:45px" role="img" aria-label="Pink blossom cluster"></div>
    <div class="brand" style="top:70px"><span class="wordmark-dot"></span><div class="wordmark">Rowlett<br>Fruit Packers</div></div>
  </div>
  <div class="panel cherry bottom-row" style="left:266px;top:304px;width:330px;height:233px">
    <div class="photo soft" style="left:-10px;top:65px;width:50px;height:55px" role="img" aria-label="Blurred cherry"></div>
    <div class="photo leaf soft" style="left:0px;top:150px;width:40px;height:60px" role="img" aria-label="Green leaf"></div>
    <div class="photo" style="left:40px;top:175px;width:55px;height:40px" role="img" aria-label="Cherries and blossom"></div>
    <div class="photo" style="left:270px;top:35px;width:40px;height:40px" role="img" aria-label="Pair of cherries"></div>
    <div class="photo" style="left:282px;top:125px;width:30px;height:30px" role="img" aria-label="Single cherry"></div>
    <div class="photo soft" style="left:235px;top:170px;width:100px;height:70px" role="img" aria-label="Large cherries"></div>
    <div class="brand" style="top:30px"><span class="wordmark-dot"></span><div class="wordmark">Rowlett<br>Fruit Packers</div><div class="slogan">From our family to yours</div><div class="legacy">LEGACY QUALITY</div></div>
  </div>
  <div class="panel cherry bottom-row" style="left:602px;top:304px;width:232px;height:233px">
    <div class="photo blossom" style="left:10px;top:80px;width:36px;height:40px" role="img" aria-label="Pink blossoms"></div>
    <div class="photo" style="left:26px;top:140px;width:50px;height:45px" role="img" aria-label="Cherries on stems"></div>
    <div class="photo soft" style="left:176px;top:115px;width:45px;height:45px" role="img" aria-label="Blurred cherry"></div>
    <div class="photo blossom" style="left:170px;top:170px;width:50px;height:45px" role="img" aria-label="Pink blossom cluster"></div>
    <div class="brand" style="top:70px"><span class="wordmark-dot"></span><div class="wordmark">Rowlett<br>Fruit Packers</div></div>
  </div>
  <div class="panel cherry bottom-row" style="left:838px;top:304px;width:330px;height:233px">
    <div class="photo soft" style="left:-10px;top:65px;width:50px;height:55px" role="img" aria-label="Blurred cherry"></div>
    <div class="photo leaf soft" style="left:0px;top:150px;width:40px;height:60px" role="img" aria-label="Green leaf"></div>
    <div class="photo" style="left:40px;top:175px;width:55px;height:40px" role="img" aria-label="Cherries and blossom"></div>
    <div class="photo" style="left:270px;top:35px;width:40px;height:40px" role="img" aria-label="Pair of cherries"></div>
    <div class="photo" style="left:282px;top:125px;width:30px;height:30px" role="img" aria-label="Single cherry"></div>
    <div class="photo soft" style="left:235px;top:170px;width:100px;height:70px" role="img" aria-label="Large cherries"></div>
    <div class="brand" style="top:30px"><span class="wordmark-dot"></span><div class="wordmark">Rowlett<br>Fruit Packers</div><div class="slogan">From our family to yours</div><div class="legacy">LEGACY QUALITY</div></div>
  </div>
</section>

<!-- Apple box -->
<section class="box apple-box">
  <div class="panel apple top-row" style="left:36px;top:616px;width:229px;height:229px">
    <div class="photo blossom" style="left:190px;top:10px;width:40px;height:70px" role="img" aria-label="Apple blossoms"></div>
    <div class="photo green-apple" style="left:-10px;top:70px;width:30px;height:30px" role="img" aria-label="Green apple"></div>
    <div class="photo soft" style="left:-10px;top:160px;width:90px;height:80px" role="img" aria-label="Blurred red apple"></div>
    <div class="photo" style="left:180px;top:135px;width:45px;height:45px" role="img" aria-label="Red apple"></div>
    <div class="photo blossom" style="left:155px;top:180px;width:55px;height:45px" role="img" aria-label="Apple blossom sprig"></div>
    <div class="brand" style="top:85px"><span class="wordmark-dot"></span><div class="wordmark">Rowlett<br>Fruit Packers</div></div>
  </div>
  <div class="panel apple top-row" style="left:270px;top:616px;width:325px;height:229px">
    <div class="photo blossom" style="left:10px;top:0px;width:60px;height:50px" role="img" aria-label="Apple blossoms"></div>
    <div class="photo" style="left:12px;top:70px;width:40px;height:40px" role="img" aria-label="Red apple"></div>
    <div class="photo blossom" style="left:10px;top:115px;width:50px;height:45px" role="img" aria-label="Blossom sprig"></div>
    <div class="photo green-apple" style="left:25px;top:170px;width:60px;height:45px" role="img" aria-label="Green apple with blossoms"></div>
    <div class="photo" style="left:260px;top:20px;width:45px;height:45px" role="img" aria-label="Red apple"></div>
    <div class="photo soft" style="left:250px;top:150px;width:90px;height:90px" role="img" aria-label="Large blurred red apple"></div>
    <div class="brand" style="top:50px"><span class="wordmark-dot"></span><div class="wordmark">Rowlett<br>Fruit Packers</div><div class="slogan">From our family to yours</div><div class="legacy">LEGACY QUALITY</div></div>
  </div>
  <div class="panel apple top-row" style="left:600px;top:616px;width:229px;height:229px">
    <div class="photo blossom" style="left:190px;top:10px;width:40px;height:70px" role="img" aria-label="Apple blossoms"></div>
    <div class="photo green-apple" style="left:-10px;top:70px;width:30px;height:30px" role="img" aria-label="Green apple"></div>
    <div class="photo soft" style="left:-10px;top:160px;width:90px;height:80px" role="img" aria-label="Blurred red apple"></div>
    <div class="photo" style="left:180px;top:135px;width:45px;height:45px" role="img" aria-label="Red apple"></div>
    <div class="photo blossom" style="left:155px;top:180px;width:55px;height:45px" role="img" aria-label="Apple blossom sprig"></div>
    <div class="brand" style="top:85px"><span class="wordmark-dot"></span><div class="wordmark">Rowlett<br>Fruit Packers</div></div>
  </div>
  <div class="panel apple top-row" style="left:834px;top:614px;width:324px;height:231px">
    <div class="photo blossom" style="left:10px;top:0px;width:60px;height:50px" role="img" aria-label="Apple blossoms"></div>
    <div class="photo" style="left:12px;top:70px;width:40px;height:40px" role="img" aria-label="Red apple"></div>
    <div class="photo blossom" style="left:10px;top:115px;width:50px;height:45px" role="img" aria-label="Blossom sprig"></div>
    <div class="photo green-apple" style="left:25px;top:170px;width:60px;height:45px" role="img" aria-label="Green apple with blossoms"></div>
    <div class="photo" style="left:260px;top:20px;width:45px;height:45px" role="img" aria-label="Red apple"></div>
    <div class="photo soft" style="left:250px;top:150px;width:90px;height:90px" role="img" aria-label="Large blurred red apple"></div>
    <div class="brand" style="top:50px"><span class="wordmark-dot"></span><div class="wordmark">Rowlett<br>Fruit Packers</div><div class="slogan">From our family to yours</div><div class="legacy">LEGACY QUALITY</div></div>
  </div>

  <div class="panel apple bottom-row" style="left:36px;top:850px;width:229px;height:230px">
    <div class="photo soft" style="left:0px;top:-20px;width:60px;height:60px" role="img" aria-label="Blurred red apple"></div>
    <div class="photo soft" style="left:175px;top:35px;width:70px;height:80px" role="img" aria-label="Blurred red apple"></div>
    <div class="photo green-apple" style="left:-10px;top:120px;width:30px;height:30px" role="img" aria-label="Green apple"></div>
    <div class="photo" style="left:50px;top:160px;width:60px;height:50px" role="img" aria-label="Pair of red apples"></div>
    <div class="photo blossom" style="left:185px;top:140px;width:40px;height:30px" role="img" aria-label="Apple blossom sprig"></div>
    <div class="brand" style="top:70px"><span class="wordmark-dot"></span><div class="wordmark">Rowlett<br>Fruit Packers</div></div>
  </div>
  <div class="panel apple bottom-row" style="left:270px;top:850px;width:325px;height:230px">
    <div class="photo" style="left:12px;top:48px;width:50px;height:50px" role="img" aria-label="Red apple with blossoms"></div>
    <div class="photo soft" style="left:-10px;top:160px;width:50px;height:80px" role="img" aria-label="Blurred red apple"></div>
    <div class="photo" style="left:60px;top:160px;width:70px;height:60px" role="img" aria-label="Pair of red apples"></div>
    <div class="photo soft" style="left:250px;top:-20px;width:80px;height:60px" role="img" aria-label="Blurred red apple"></div>
    <div class="photo" style="left:270px;top:110px;width:55px;height:60px" role="img" aria-label="Apples with blossoms"></div>
    <div class="brand" style="top:30px"><span class="wordmark-dot"></span><div class="wordmark">Rowlett<br>Fruit Packers</div><div class="slogan">From our family to yours</div><div class="legacy">LEGACY QUALITY</div></div>
  </div>
  <div class="panel apple bottom-row" style="left:600px;top:850px;width:229px;height:230px">
    <div class="photo soft" style="left:0px;top:-20px;width:60px;height:60px" role="img" aria-label="Blurred red apple"></div>
    <div class="photo soft" style="left:175px;top:35px;width:70px;height:80px" role="img" aria-label="Blurred red apple"></div>
    <div class="photo green-apple" style="left:-10px;top:120px;width:30px;height:30px" role="img" aria-label="Green apple"></div>
    <div class="photo" style="left:50px;top:160px;width:60px;height:50px" role="img" aria-label="Pair of red apples"></div>
    <div class="photo blossom" style="left:185px;top:140px;width:40px;height:30px" role="img" aria-label="Apple blossom sprig"></div>
    <div class="brand" style="top:70px"><span class="wordmark-dot"></span><div class="wordmark">Rowlett<br>Fruit Packers</div></div>
  </div>
  <div class="panel apple bottom-row" style="left:834px;top:848px;width:324px;height:230px">
    <div class="photo" style="left:12px;top:48px;width:50px;height:50px" role="img" aria-label="Red apple with blossoms"></div>
    <div class="photo soft" style="left:-10px;top:160px;width:50px;height:80px" role="img" aria-label="Blurred red apple"></div>
    <div class="photo" style="left:60px;top:160px;width:70px;height:60px" role="img" aria-label="Pair of red apples"></div>
    <div class="photo soft" style="left:250px;top:-20px;width:80px;height:60px" role="img" aria-label="Blurred red apple"></div>
    <div class="photo" style="left:270px;top:110px;width:55px;height:60px" role="img" aria-label="Apples with blossoms"></div>
    <div class="brand" style="top:30px"><span class="wordmark-dot"></span><div class="wordmark">Rowlett<br>Fruit Packers</div><div class="slogan">From our family to yours</div><div class="legacy">LEGACY QUALITY</div></div>
  </div>
</section>

</body>
</html>
```